Contractor Business Card Design

Looking to have a card made that has a bold description of (KITCHENS, BASEMENTS, BATHROOMS)

Definition and layers a plus

Contact info is;

Mark T. Ellery
Elm Prairie, MN 55990
Cell: 612-555-0147
website: www.cobaltfinishworks.example
Email: cobaltfinishworksmn@mailbox.example

colors: red, black, gray, white

Contact Information for Business Card

Contact info is;

Mark T. Ellery
Elm Prairie, MN 55990
Cell: 612-555-0147

Colors
ec1f27

Requirements
Must have
• Looking for layers and definition
Nice to have
• Cards are planned to be printed on plastic cards

```html
<!DOCTYPE html>
<html lang="en">
<head>
<meta charset="utf-8">
<title>Cobalt Finish Works – Business Card</title>
<link rel="stylesheet" href="https://fonts.googleapis.com/css2?family=Red+Hat+Display:wght@500;600;700&display=swap">
<style>
  :root {
    --backdrop: #9b9b9b;
    --ink: #141416;
    --paper: #ffffff;
    --red: #dd2926;
    --text-dark: #2b2b2e;
  }
  html, body {
    margin: 0;
    padding: 0;
    width: 1021px;
    height: 1200px;
    overflow: hidden;
    background: var(--backdrop);
    font-family: "Red Hat Display", Arial, sans-serif;
  }
  .card {
    position: absolute;
    width: 753px;
    height: 429px;
    display: block;
  }
  .card--front { left: 134px; top: 119px; }
  .card--back  { left: 131px; top: 651px; }
  .card text { font-family: "Red Hat Display", Arial, sans-serif; }
  .services text { fill: var(--paper); font-size: 32px; font-weight: 500; }
  .services circle { fill: var(--red); }
  .brand-front { fill: var(--paper); font-weight: 700; }
  .brand-back { fill: var(--ink); font-weight: 700; }
  .holder-name { fill: var(--red); font-size: 64px; font-weight: 600; }
  .holder-role { fill: var(--text-dark); font-size: 32px; font-weight: 500; }
  .contact-line { fill: var(--text-dark); font-size: 32px; font-weight: 500; }
  .contact-icon { fill: var(--red); }
</style>
</head>
<body>

<svg class="card card--front" viewBox="0 0 1301 741" aria-label="Card front">
  <defs>
    <clipPath id="front-clip"><rect width="1301" height="741"/></clipPath>
  </defs>
  <rect class="card-base" width="1301" height="741" fill="var(--ink)"/>
  <g clip-path="url(#front-clip)">
    <path class="swoosh-white" fill="var(--paper)" fill-rule="evenodd"
      d="M-238,821 a563,563 0 1,0 1126,0 a563,563 0 1,0 -1126,0 Z
         M-251,824 a541,541 0 1,0 1082,0 a541,541 0 1,0 -1082,0 Z"/>
    <path class="swoosh-red" fill="var(--red)"
      d="M0,367 Q290,190 645,432 Q320,210 0,440 Z"/>
  </g>

  <g class="services">
    <circle cx="103" cy="549" r="7"/>
    <text x="123" y="559">KITCHENS</text>
    <circle cx="103" cy="599" r="7"/>
    <text x="123" y="609">BASEMENTS</text>
    <circle cx="103" cy="648" r="7"/>
    <text x="123" y="658">BATHROOMS</text>
  </g>

  <g class="brand">
    <circle cx="1069" cy="166" r="96" fill="none" stroke="var(--paper)" stroke-width="6"/>
    <text class="brand-front" x="1069" y="350" text-anchor="middle" font-size="70" letter-spacing="2">COBALT</text>
    <text class="brand-front" x="1069" y="390" text-anchor="middle" font-size="24" letter-spacing="10">FINISH WORKS</text>
  </g>
</svg>

<svg class="card card--back" viewBox="0 0 1301 741" aria-label="Card back">
  <defs>
    <clipPath id="back-clip"><rect width="1301" height="741"/></clipPath>
  </defs>
  <rect class="card-base" width="1301" height="741" fill="var(--paper)"/>
  <g clip-path="url(#back-clip)">
    <path class="swoosh-black" fill="var(--ink)" fill-rule="evenodd"
      d="M-238,75 a563,563 0 1,0 1126,0 a563,563 0 1,0 -1126,0 Z
         M-190,101 a515,515 0 1,0 1030,0 a515,515 0 1,0 -1030,0 Z"/>
    <path class="swoosh-red" fill="var(--red)"
      d="M0,520 Q300,720 670,440 Q330,704 0,460 Z"/>
  </g>

  <g class="holder">
    <text class="holder-name" x="92" y="148">Mark T. Ellery</text>
    <text class="holder-role" x="94" y="190">Co-Founder</text>
  </g>

  <g class="contacts">
    <path class="contact-icon" transform="translate(94,236)"
      d="M5,2 L10,1 L13,8 L9,11 Q12,17 17,20 L20,16 L27,19 L26,24 Q24,27 19,26 Q7,22 2,9 Q1,4 5,2 Z"/>
    <text class="contact-line" x="131" y="261">612-555-0147</text>
    <g transform="translate(94,284)">
      <rect class="contact-icon" width="26" height="18" rx="1"/>
      <path d="M1,1 L13,11 L25,1 M1,17 L9,9 M25,17 L17,9" stroke="var(--paper)" stroke-width="2" fill="none"/>
    </g>
    <text class="contact-line" x="131" y="304">cobaltfinishworksmn@mailbox.example</text>
    <g transform="translate(107,333)">
      <circle class="contact-icon" r="13"/>
      <path d="M-13,0 H13 M0,-13 V13 M-7,-10 Q0,0 -7,10 M7,-10 Q0,0 7,10" stroke="var(--paper)" stroke-width="1.6" fill="none"/>
    </g>
    <text class="contact-line" x="131" y="346">www.cobaltfinishworks.example</text>
    <path class="contact-icon" fill-rule="evenodd" transform="translate(94,360)"
      d="M13,34 Q0,18 0,13 A13,13 0 0 1 26,13 Q26,18 13,34 Z M13,8 A5,5 0 1 0 13,18 A5,5 0 1 0 13,8 Z"/>
    <text class="contact-line" x="131" y="388">Elm Prairie, MN 55990</text>
  </g>

  <g class="brand">
    <circle cx="1057" cy="439" r="94" fill="none" stroke="var(--ink)" stroke-width="6"/>
    <text class="brand-back" x="1057" y="615" text-anchor="middle" font-size="70" letter-spacing="2">COBALT</text>
    <text class="brand-back" x="1057" y="655" text-anchor="middle" font-size="24" letter-spacing="10">FINISH WORKS</text>
  </g>
</svg>

</body>
</html>
```